Corvane Systems Modern, Sleek One Pager/Slick Sheet

Creative Brief: One-Pager Design for Corvane Systems
Project Overview:
We are seeking a highly skilled graphic designer to create a modern, sleek, and visually impactful one-pager (slick sheet) for Corvane Systems, a leading company in the defense and aerospace sector. This slick sheet will serve as a high-level marketing asset, designed to quickly capture attention and communicate Corvane Systems’s cutting-edge capabilities, technological expertise, and commitment to national security and innovation.
Key Objectives:
Establish a high-tech, sophisticated look and feel that aligns with the defense and aerospace industries.
Highlight Corvane Systems’s core competencies, key services, and differentiators with clear and concise messaging.
Ensure the design supports easy readability and quick scanning of critical information.
Incorporate strong visual hierarchy and premium, professional aesthetics.
Design Specifications:
Format: Single-page, print and digital distribution-ready (PDF format).
Layout Style: Clean, minimalist, and balanced with ample white space.
Typography: Modern, sans-serif fonts that convey innovation and strength.
Color Palette: Incorporate Corvane Systems’s brand colors (navy blue, steel gray, white, accents of metallic or deep reds if applicable).
Imagery: Use high-resolution imagery that reflects advanced technology, aerospace engineering, and national defense. Subtle technical graphics, schematics, or abstract patterns are acceptable to enhance visual interest without clutter.
Content Elements (To Be Provided):
Company Logo and Tagline
Key Capabilities and Service Offerings
Differentiators and Core Competencies
Contact Information
Visual Icons or Infographics for Quick Reference (if applicable)
Tone & Mood:
Professional, authoritative, and cutting-edge
Emphasizes trust, innovation, and mission-critical solutions
Appeals to government and defense industry stakeholders
Deliverables:
Final high-resolution print-ready PDF
Digital-friendly PDF optimized for email and web use
Source files (Adobe Illustrator, InDesign, or equivalent)
Target Market(s)
Defense/Aviation
Industry/Entity Type
Defense/Aviation
Look and feel

```html
<!DOCTYPE html>
<html lang="en">
<head>
<meta charset="utf-8">
<title>Corvane Systems – Capabilities Sheet</title>
<link rel="stylesheet" href="https://fonts.googleapis.com/css2?family=Orbitron:wght@700;900&family=Poppins:wght@400;500;600;700&display=swap">
<style>
  :root {
    --navy: #0c0c3d;
    --navy-deep: #07073a;
    --red: #8c1020;
    --black: #0b0b0b;
    --charcoal: #2a2a2a;
    --paper: #efefef;
    --ink: #161616;
    --rule: #9a9a9a;
    --white: #ffffff;
  }
  * { box-sizing: border-box; margin: 0; padding: 0; }
  html, body { width: 900px; height: 1200px; overflow: hidden; }
  body {
    font-family: "Poppins", sans-serif;
    color: var(--ink);
    background: var(--paper);
  }
  .sheet {
    position: relative;
    width: 900px;
    height: 1200px;
    background: linear-gradient(135deg, #f4f4f4 0%, #ececec 45%, #f2f2f2 70%, #e9e9e9 100%);
    overflow: hidden;
  }
  .abs { position: absolute; }

  /* Hero panel */
  .hero-panel {
    left: 64px; top: 0; width: 335px; height: 451px;
    background: linear-gradient(180deg, #1c1c1c 0%, #2e2e2e 45%, #0d0d0d 100%);
  }
  .brand {
    left: 64px; top: 70px; width: 335px;
    display: flex; align-items: center; justify-content: center; gap: 10px;
    color: var(--white);
    font-family: "Poppins", sans-serif; font-weight: 500;
    font-size: 21px; letter-spacing: 3px; text-transform: uppercase;
  }
  .brand-square { width: 16px; height: 16px; background: var(--white); }
  .aircraft-photo {
    left: 0; top: 320px; width: 427px; height: 187px;
    background: radial-gradient(ellipse at 55% 45%, #f4f4f4 0%, #cfd2d6 45%, rgba(120,120,120,0.25) 75%, rgba(239,239,239,0) 100%);
  }

  /* Headline */
  .headline {
    left: 440px; top: 62px;
    font-family: "Orbitron", sans-serif; font-weight: 900;
    color: var(--black); font-size: 39px; line-height: 37px; letter-spacing: 0.5px;
  }
  .headline-accent {
    left: 440px; top: 140px;
    font-family: "Orbitron", sans-serif; font-weight: 900;
    color: var(--red); font-size: 21.5px; letter-spacing: 0.5px;
  }
  .tagline-pill {
    left: 440px; top: 171px; height: 25px; padding: 0 12px 0 12px;
    background: var(--navy); color: var(--white);
    border-left: 4px solid var(--red); border-radius: 0 13px 13px 0;
    font-weight: 700; font-size: 11.5px; line-height: 25px;
  }

  /* Mission */
  .section-label {
    font-family: "Orbitron", sans-serif; font-weight: 700;
    color: var(--red); letter-spacing: 3px;
  }
  .mission-label { left: 442px; top: 222px; font-size: 12px; }
  .mission-text {
    left: 442px; top: 244px; width: 370px;
    font-size: 11.3px; line-height: 14.5px;
  }
  .photo { top: 328px; width: 128px; height: 123px; border: 1px solid #777; }
  .photo-drone { left: 441px; background: linear-gradient(160deg, #e6e6e6, #8a8a8a 55%, #cfcfcf); }
  .photo-team  { left: 575px; background: linear-gradient(160deg, #3a3a3a, #9d9d9d 55%, #1a1a1a); }
  .photo-radar { left: 708px; background: radial-gradient(circle at 60% 55%, #8a8a8a 0%, #2b2b2b 45%, #050505 100%); }

  /* Aviation services */
  .services-title {
    left: 442px; top: 473px;
    font-family: "Orbitron", sans-serif; font-weight: 900;
    color: var(--red); font-size: 22.5px; letter-spacing: 1px;
  }
  .service { left: 442px; width: 400px; display: flex; gap: 17px; }
  .service-icon { width: 45px; height: 45px; flex: none; }
  .service-title { color: var(--navy); font-weight: 600; font-size: 16px; line-height: 20px; }
  .service-desc { margin-top: 8px; font-size: 11.3px; line-height: 14.3px; width: 300px; }
  .divider { left: 447px; width: 386px; border-top: 1px dashed var(--rule); }

  /* Mission area */
  .tile {
    width: 138px; height: 141px; color: var(--white);
    padding: 30px 8px 0 20px; overflow: hidden;
    font-weight: 500; font-size: 12.3px; line-height: 14.6px;
  }
  .tile-dark { background: var(--black); }
  .tile-navy { background: var(--navy-deep); }
  .tile-number {
    position: absolute; right: -2px; bottom: -6px;
    font-weight: 700; font-size: 37px; line-height: 40px;
    color: rgba(255,255,255,0.16);
  }
  .mission-area-title {
    left: 215px; top: 614px;
    font-family: "Orbitron", sans-serif; font-weight: 900; color: var(--red);
  }
  .mission-area-title .small { display: block; font-size: 20px; line-height: 24px; }
  .mission-area-title .large { display: block; font-size: 28.5px; line-height: 28px; }

  /* Management */
  .management-title {
    left: 64px; top: 988px;
    font-family: "Orbitron", sans-serif; font-weight: 900;
    color: var(--red); font-size: 20px; line-height: 24px; letter-spacing: 0.5px;
  }
  .mgmt-item { width: 140px; font-weight: 500; font-size: 12.3px; line-height: 14.6px; }
  .mgmt-hrule { left: 60px; top: 1093px; width: 301px; border-top: 1px dashed var(--rule); }
  .mgmt-vrule { left: 209px; top: 1048px; height: 90px; border-left: 1px dashed var(--rule); }

  /* Contact */
  .contact-prompt {
    left: 442px; top: 1057px;
    font-weight: 700; font-size: 20.5px; line-height: 26px; color: var(--red);
  }
  .contact-prompt .dark { color: var(--navy); }
  .contact-list { left: 606px; top: 1050px; list-style: none; }
  .contact-list li { display: flex; align-items: center; gap: 9px; color: var(--navy); }
  .contact-icon { width: 22px; height: 22px; flex: none; }
  .contact-phone { font-weight: 700; font-size: 21.5px; height: 30px; }
  .contact-line { font-weight: 500; font-size: 14.5px; height: 26px; }
</style>
</head>
<body>
<main class="sheet">

  <div class="abs hero-panel"></div>
  <div class="abs brand"><span class="brand-square"></span>Corvane Systems</div>
  <div class="abs aircraft-photo" role="img" aria-label="Photo of a white twin-turboprop special-mission aircraft on the ramp"></div>

  <h1 class="abs headline">PROVIDING<br>TOP-NOTCH</h1>
  <div class="abs headline-accent">SERVICES TAILORED</div>
  <div class="abs tagline-pill">TO MEET YOUR BUSINESS NEEDS</div>

  <h2 class="abs section-label mission-label">OUR MISSION</h2>
  <p class="abs mission-text">Our experienced team is committed to providing top-notch services tailored to meet your business needs. We strive to deliver exceptional results, exceeding expectations every step of the way.</p>

  <div class="abs photo photo-drone" role="img" aria-label="Black and white photo of a surveillance drone"></div>
  <div class="abs photo photo-team" role="img" aria-label="Black and white photo of operators in the field"></div>
  <div class="abs photo photo-radar" role="img" aria-label="Abstract radar interface graphic"></div>

  <h2 class="abs services-title">AVIATION SERVICES</h2>

  <div class="abs service" style="top:523px">
    <svg class="service-icon" viewBox="0 0 45 45" aria-hidden="true">
      <circle cx="20" cy="26" r="17" fill="none" stroke="var(--red)" stroke-width="4"/>
      <circle cx="20" cy="26" r="10" fill="none" stroke="var(--red)" stroke-width="4"/>
      <circle cx="20" cy="26" r="4" fill="var(--red)"/>
      <path d="M20 26 L38 8" stroke="var(--navy)" stroke-width="3"/>
      <path d="M35 4 L42 2 L40 10 Z" fill="var(--navy)"/>
    </svg>
    <div>
      <h3 class="service-title">ISR Special Mission</h3>
      <p class="service-desc">Global Intelligence, Surveillance, and Reconnaissance providing creative solutions in multi-domain operations</p>
    </div>
  </div>
  <div class="abs divider" style="top:611px"></div>

  <div class="abs service" style="top:626px">
    <svg class="service-icon" viewBox="0 0 45 45" aria-hidden="true">
      <path d="M5 3 H25 L34 12 V42 H5 Z" fill="var(--red)"/>
      <path d="M10 14 H22 M10 20 H26 M10 26 H18 M10 32 H18" stroke="#fff" stroke-width="2.5"/>
      <circle cx="28" cy="31" r="7" fill="#fff" stroke="var(--navy)" stroke-width="3"/>
      <path d="M33 36 L40 43" stroke="var(--navy)" stroke-width="4"/>
    </svg>
    <div>
      <h3 class="service-title">Research and Development</h3>
      <p class="service-desc">Specialize in testing of new technologies for future ISR construct, next-generation warfighting capabilities</p>
    </div>
  </div>
  <div class="abs divider" style="top:714px"></div>

  <div class="abs service" style="top:728px">
    <svg class="service-icon" viewBox="0 0 45 45" aria-hidden="true">
      <path d="M3 3 H24 L30 9 V40 H3 Z" fill="var(--red)"/>
      <path d="M8 12 H22 M8 18 H22 M8 24 H16" stroke="#fff" stroke-width="2.5"/>
      <path d="M20 20 L30 14 L36 22 L28 28 Z" fill="var(--navy)"/>
      <path d="M30 26 L42 40" stroke="var(--navy)" stroke-width="5"/>
    </svg>
    <div>
      <h3 class="service-title">CONUS Efforts</h3>
      <p class="service-desc">State/Federal Law Enforcement, Natural Disaster, Search and Rescue, Specialized SOF programs</p>
    </div>
  </div>
  <div class="abs divider" style="top:802px"></div>

  <div class="abs service" style="top:819px">
    <svg class="service-icon" viewBox="0 0 45 45" aria-hidden="true">
      <path d="M22 2 L40 8 V22 C40 33 32 40 22 44 C12 40 4 33 4 22 V8 Z" fill="var(--navy)"/>
      <path d="M22 7 L35 11 V22 C35 30 29 35 22 38 C15 35 9 30 9 22 V11 Z" fill="#fff"/>
      <circle cx="22" cy="21" r="8" fill="var(--red)"/>
      <path d="M18 21 L21 24 L26 18" stroke="#fff" stroke-width="1.8" fill="none"/>
    </svg>
    <div>
      <h3 class="service-title">OCONUS Efforts</h3>
      <p class="service-desc">Streamlining international collaboration to shape the global landscape and safeguarding our nation and allies</p>
    </div>
  </div>
  <div class="abs divider" style="top:910px"></div>

  <div class="abs service" style="top:927px">
    <svg class="service-icon" viewBox="0 0 45 45" aria-hidden="true">
      <path d="M38 4 C41 3 42 4 41 7 L33 16 L38 34 L34 37 L26 22 L18 30 L19 36 L16 38 L13 31 L6 28 L8 25 L14 26 L22 18 L8 10 L11 6 L29 11 Z" fill="var(--navy)"/>
      <path d="M4 36 L10 30 M7 40 L12 35 M11 42 L15 38" stroke="var(--red)" stroke-width="2"/>
    </svg>
    <div>
      <h3 class="service-title">Aviation Training</h3>
      <p class="service-desc">Solving complex problems with dynamic solutions for future warfighters</p>
    </div>
  </div>

  <!-- Mission area grid -->
  <div class="abs tile tile-dark" style="left:64px;top:529px;padding-top:40px">Manned ISR<br>for Actionable<br>Intelligence<span class="tile-number">01</span></div>
  <div class="abs mission-area-title"><span class="small">MISSION</span><span class="large">AREA</span></div>
  <div class="abs tile tile-navy" style="left:64px;top:677px">Maintenance<br>Services/<br>Aviation<br>Training<br>Services<span class="tile-number">02</span></div>
  <div class="abs tile tile-dark" style="left:208px;top:677px;padding-top:46px">Modular<br>Pod<br>Capabilities<span class="tile-number">03</span></div>
  <div class="abs tile tile-dark" style="left:64px;top:824px;padding-top:46px">Electromagnetic<br>Warfare<br>Solutions<span class="tile-number">04</span></div>
  <div class="abs tile tile-navy" style="left:208px;top:824px;padding-top:54px">SIGINT<br>Solutions<span class="tile-number">05</span></div>

  <h2 class="abs management-title">ADAPTIVE &amp; DYNAMIC<br>MANAGEMENT</h2>
  <div class="abs mgmt-item" style="left:64px;top:1051px">Program<br>Management</div>
  <div class="abs mgmt-item" style="left:226px;top:1051px">Administrative<br>Services</div>
  <div class="abs mgmt-item" style="left:64px;top:1103px">Event Management<br>&amp; Execution</div>
  <div class="abs mgmt-item" style="left:226px;top:1103px">Enterprise IT<br>Services</div>
  <div class="abs mgmt-hrule"></div>
  <div class="abs mgmt-vrule"></div>

  <p class="abs contact-prompt">Contact<br>us for more<br><span class="dark">information</span></p>
  <ul class="abs contact-list">
    <li class="contact-phone">
      <svg class="contact-icon" viewBox="0 0 22 22" aria-hidden="true"><circle cx="11" cy="11" r="11" fill="var(--navy)"/><path d="M7 6 L9 6 L10 9 L8.6 10 C9.3 11.5 10.5 12.7 12 13.4 L13 12 L16 13 L16 15 C16 15.6 15.5 16 15 16 C10 16 6 12 6 7 C6 6.5 6.4 6 7 6 Z" fill="#fff"/></svg>
      (555) 014-2870
    </li>
    <li class="contact-line">
      <svg class="contact-icon" viewBox="0 0 22 22" aria-hidden="true"><circle cx="11" cy="11" r="11" fill="var(--navy)"/><rect x="6" y="7.5" width="10" height="7" fill="none" stroke="#fff" stroke-width="1.3"/><path d="M6 7.5 L11 11.5 L16 7.5" fill="none" stroke="#fff" stroke-width="1.3"/></svg>
      info@corvanesystems.com
    </li>
    <li class="contact-line">
      <svg class="contact-icon" viewBox="0 0 22 22" aria-hidden="true"><circle cx="11" cy="11" r="11" fill="var(--navy)"/><circle cx="11" cy="11" r="5.5" fill="none" stroke="#fff" stroke-width="1.2"/><path d="M5.5 11 H16.5 M11 5.5 C8.5 8 8.5 14 11 16.5 M11 5.5 C13.5 8 13.5 14 11 16.5" fill="none" stroke="#fff" stroke-width="1.1"/></svg>
      www.corvanesystems.com
    </li>
  </ul>

</main>
</body>
</html>
```